Paramount Vigor Product design

We need a bottle design for our product. Paramount Vigor is a Gaming Nootropic made to increase Energy, Focus, Reaction time, and Clarity of an eSport gamer. It will be 40 servings a bottle. Currently, all the ingredients haven't been finalized so after the competition is over we will have to work with the designer to also make an ingredients label for the back of it. For the flavor, we will call it tundra mist.

The attachments included:. The velvet lanterns picture as a font style I like for the logo.
The Z BOOST QUENCH PICTURE IS WHAT WE WANT OUR DESIGN to look like something similar a clean and simple design that stands out!

Z Boost bottle is what our biggest competitors product looks like. The paramount vigor picture as the current logo we are using but can be changed.

Overall the pictures are just some references for what I could possibly want the design to look like however, I'm open to your designer's ideas and concepts you think would make for a cool looking Gaming Nootropic product bottle design. I appreciate everyone working on this and look forward to seeing your designs have a great day!

Target Market(s)

Gamers between the ages of 18-30

Industry/Entity Type

Health And Wellness

Requirements
Must have
• Paramount Vigor logo, state that it is for energy, focus, reaction, and clarity. state 40 serivngs. state flavor.

```html
<!DOCTYPE html>
<html lang="en">
<head>
<meta charset="utf-8">
<title>Paramount Vigor – Tundra Mist Label</title>
<link rel="stylesheet" href="https://fonts.googleapis.com/css2?family=Exo+2:ital,wght@0,500;0,600;1,600;1,700;1,800&family=Saira+Semi+Condensed:wght@600&family=Oswald:wght@700&family=Open+Sans:wght@400&display=swap">
<style>
  :root {
    --royal: #2a51a3;
    --royal-deep: #24489a;
    --tile: #b3d6f2;
    --ink: #111111;
    --white: #ffffff;
    --mist: #eef5fc;
  }
  * { margin: 0; padding: 0; box-sizing: border-box; }
  html, body { width: 1200px; height: 951px; overflow: hidden; background: var(--white); }
  .label {
    position: relative;
    width: 1200px;
    height: 951px;
    overflow: hidden;
    background: linear-gradient(180deg, var(--white) 0%, var(--white) 45%, var(--mist) 64%);
    font-family: "Exo 2", sans-serif;
  }
  .tile-band {
    position: absolute;
    left: 0; top: 32px;
    width: 1200px; height: 148px;
    background: linear-gradient(180deg, var(--tile) 0%, #c6e0f6 50%, var(--tile) 100%);
    opacity: 0.75;
  }
  .servings-tab {
    position: absolute;
    left: 956px; top: 0;
    width: 136px; height: 418px;
    background: var(--royal);
    border-radius: 0 0 40px 40px;
    color: var(--white);
    font-family: "Oswald", sans-serif;
    font-weight: 700;
    text-align: center;
  }
  .servings-count { position: absolute; left: 0; right: 0; top: 284px; font-size: 70px; line-height: 1; }
  .servings-word { position: absolute; left: 0; right: 0; top: 364px; font-size: 25px; line-height: 1; }
  .brand-name {
    position: absolute;
    left: 150px; top: 280px;
    font-family: "Exo 2", sans-serif;
    font-weight: 500;
    font-size: 74px;
    line-height: 1;
    color: var(--ink);
    letter-spacing: 1px;
    white-space: nowrap;
  }
  .audience {
    position: absolute;
    left: 160px; top: 448px;
    font-style: italic;
    font-weight: 800;
    font-size: 50px;
    line-height: 1;
    letter-spacing: 6px;
    color: var(--royal);
    white-space: nowrap;
  }
  .base-band { position: absolute; left: 0; top: 614px; width: 1200px; height: 337px; }
  .stat {
    position: absolute;
    top: 624px;
    width: 100px;
    text-align: center;
    color: var(--white);
    font-style: italic;
  }
  .stat-value { display: block; font-weight: 800; font-size: 50px; line-height: 1; }
  .stat-label { display: block; font-weight: 600; font-size: 13px; line-height: 1; margin-top: 2px; }
  .flavor {
    position: absolute;
    left: 612px; top: 632px;
    font-style: italic;
    font-weight: 800;
    font-size: 54px;
    line-height: 1;
    letter-spacing: 4px;
    color: var(--white);
    white-space: nowrap;
  }
  .benefits {
    position: absolute;
    left: 0; right: 0; top: 744px;
    text-align: center;
    font-family: "Saira Semi Condensed", "Arial Narrow", sans-serif;
    font-weight: 600;
    font-size: 44px;
    line-height: 1;
    letter-spacing: 4px;
    color: var(--white);
    white-space: nowrap;
  }
  .product-facts {
    position: absolute;
    left: 0; right: 0; top: 808px;
    text-align: center;
    font-family: "Open Sans", sans-serif;
    font-size: 24px;
    line-height: 1.4;
    letter-spacing: 1px;
    color: var(--white);
    white-space: nowrap;
  }
</style>
</head>
<body>
<main class="label">
  <div class="tile-band" role="img" aria-label="Rows of slanted light blue tiles"></div>

  <div class="servings-tab">
    <span class="servings-count">40</span>
    <span class="servings-word">servings</span>
  </div>

  <h1 class="brand-name">PARAMOUNT VIGOR</h1>
  <p class="audience">FOR E-SPORT GAMERS</p>

  <svg class="base-band" viewBox="0 0 1200 337" width="1200" height="337" aria-hidden="true">
    <rect x="0" y="0" width="1200" height="337" fill="var(--royal)"/>
    <polygon points="207,0 220,0 203,80 190,80" fill="var(--white)"/>
    <polygon points="333,0 346,0 329,80 316,80" fill="var(--white)"/>
    <polygon points="459,0 600,0 576,80 438,80" fill="var(--white)"/>
  </svg>

  <div class="stat" style="left:90px"><span class="stat-value">0</span><span class="stat-label">SUGAR</span></div>
  <div class="stat" style="left:212px"><span class="stat-value">0</span><span class="stat-label">CALORIES</span></div>
  <div class="stat" style="left:338px"><span class="stat-value">0</span><span class="stat-label">CAFFEINE</span></div>

  <p class="flavor">TUNDRA MIST</p>
  <p class="benefits">ENERGY | FOCUS | REACTION | CLARITY</p>
  <p class="product-facts">Dietary Supplement | Net Weight 12 OZ (118g)</p>
</main>
</body>
</html>
```